whitening syringe artwork design

3ml syringe with silkscreen printing:
sample:
https://www.shopvarnex-example.com/Bravo-Nerval-Whitening-Syringes-Carbamide/item/Q47261KD9X/ref=lst_2_4?cid=7PK92LX04QWRT&dflag=1&keywords=whitening+syringes&qid=1598274410&sprefix=whitening+sy%2Caps%2C150&sr=4-2
inside the writing:
"teeth whitening gel " change to "Solivène WHITENING GEL"
"Advanced formula" change to our logo and "Not all gels are created equal. "

additional requirements:
Inches: 2.01" wide x 1.34" around

CM: 5.1cm wide x 3.4cm around

See attached template: Generic_Syringe Labels 3ml_Silkscreen.pdf

- Leave the volume gage where it is, so it prints correctly on the syringe

- Feel free to change the color and font style

- An "identifying marker" is required: Teeth Whitening Syringe or Teeth Whitening Gel (for example)

- Replace "Teeth Whitening Gel - Advanced Formula" with your text and logo - it is there as a placeholder

-We require PDF files created to print ready specifications. Color images should be down-sampled to 300DPI

-Please provide us your Chromidex color references for the color used in your artwork

https://www.chromidex-example.com/color-finder#/pick?chromidexBook=chromidexSolidCoatedV3M2

-Please ensure that all fonts are embedded in the PDF document or make sure you convert fonts to outlines to prevent any issues with fonts (AI-Type-Create Outlines)

We will need your print ready artwork in a high resolution PDF file

Target Market(s)

teeth whitening ecommerce

Requirements
Must have
• follow the guide document, and add text I want, color code from Chromidex is provided

```html
<!DOCTYPE html>
<html lang="en">
<head>
<meta charset="utf-8">
<title>Solivène Whitening Gel – 3 ml Syringe Label</title>
<link rel="stylesheet" href="https://fonts.googleapis.com/css2?family=Fredoka:wght@600&family=Alegreya+Sans:ital,wght@1,700&family=Roboto+Condensed:wght@400;700&display=swap">
<style>
  :root {
    --label-bg: #ffffff;
    --brand-blush: #f9b9ab;
    --ink-slate: #4a4e57;
  }
  html, body {
    margin: 0;
    padding: 0;
    width: 1200px;
    height: 917px;
    overflow: hidden;
    background: var(--label-bg);
  }
  .syringe-label {
    position: relative;
    width: 1200px;
    height: 917px;
    background: var(--label-bg);
  }
  .brand-lockup {
    position: absolute;
    left: 192px;
    top: 206px;
    display: flex;
    align-items: baseline;
    white-space: nowrap;
  }
  .brand-name {
    font-family: "Fredoka", sans-serif;
    font-weight: 600;
    font-size: 112px;
    line-height: 1;
    color: var(--brand-blush);
    letter-spacing: 1px;
  }
  .product-identifier {
    margin-left: 22px;
    font-family: "Fredoka", sans-serif;
    font-weight: 600;
    font-size: 47px;
    line-height: 1;
    color: var(--ink-slate);
    letter-spacing: 1px;
  }
  .tagline {
    position: absolute;
    left: 230px;
    top: 326px;
    margin: 0;
    font-family: "Alegreya Sans", sans-serif;
    font-style: italic;
    font-weight: 700;
    font-size: 55px;
    line-height: 1;
    color: var(--ink-slate);
    white-space: nowrap;
  }
  .volume-gauge {
    position: absolute;
    left: 0;
    top: 0;
  }
  .gauge-tick {
    stroke: var(--ink-slate);
    stroke-width: 6;
  }
  .gauge-value {
    font-family: "Roboto Condensed", sans-serif;
    font-weight: 700;
    font-size: 40px;
    fill: var(--ink-slate);
  }
  .gauge-unit {
    font-family: "Roboto Condensed", sans-serif;
    font-weight: 400;
    font-size: 29px;
    fill: var(--ink-slate);
  }
</style>
</head>
<body>
<main class="syringe-label">
  <div class="brand-lockup">
    <span class="brand-name">Solivène</span>
    <span class="product-identifier">WHITENING GEL</span>
  </div>
  <p class="tagline">Not all gels are created equal.</p>

  <svg class="volume-gauge" width="1200" height="917" viewBox="0 0 1200 917" aria-label="Volume gauge, 0 to 3 ml">
    <line class="gauge-tick" x1="176" y1="548" x2="176" y2="662"/>
    <line class="gauge-tick" x1="302" y1="593" x2="302" y2="662"/>
    <line class="gauge-tick" x1="428" y1="548" x2="428" y2="662"/>
    <line class="gauge-tick" x1="572" y1="593" x2="572" y2="662"/>
    <line class="gauge-tick" x1="716" y1="548" x2="716" y2="662"/>
    <line class="gauge-tick" x1="842" y1="593" x2="842" y2="662"/>
    <line class="gauge-tick" x1="970" y1="548" x2="970" y2="662"/>

    <text class="gauge-value" transform="translate(302,516) rotate(-90)" text-anchor="end" dominant-baseline="central" font-size="30">½</text>
    <text class="gauge-value" transform="translate(428,514) rotate(-90)" text-anchor="end" dominant-baseline="central">1</text>
    <text class="gauge-value" transform="translate(572,514) rotate(-90)" text-anchor="end" dominant-baseline="central">1½</text>
    <text class="gauge-value" transform="translate(716,514) rotate(-90)" text-anchor="end" dominant-baseline="central">2</text>
    <text class="gauge-value" transform="translate(842,514) rotate(-90)" text-anchor="end" dominant-baseline="central">2½</text>
    <text class="gauge-value" transform="translate(970,514) rotate(-90)" text-anchor="end" dominant-baseline="central">3</text>
    <text class="gauge-unit" transform="translate(998,650) rotate(-90)" text-anchor="start" dominant-baseline="central">ml/cc</text>
  </svg>
</main>
</body>
</html>
```